Hip Surgeon needs a web page re-design.

I have a web page to provide information about the diseases of the hip joint for the patients from my private practice since 2008. I need a re-design job for a fresh new look.
We have made a new logo and a new stationery design here in CraftLoomery (please see the uploaded files) and I want to make my web page look-alike the new design concepts.
I like the color blue and tones of blue, matching my logo and stationery.
I don't like "busy" designs. It must be clean, elegant and ease to read. The final design should be "mobile friendly" if possible.
Please visit my website www.pontevivaclinica.com.br to take a look and get some inspiration.

```html
<!DOCTYPE html>
<html lang="pt-BR">
<head>
<meta charset="utf-8">
<title>Dr. Rafael M. Andrade – Cirurgia do Quadril</title>
<link rel="stylesheet" href="https://fonts.googleapis.com/css2?family=Open+Sans:wght@400;600;700&display=swap">
<style>
:root{
  --page:#f4f4f4;
  --blue:#1a73ba;
  --dark:#2d2d2d;
  --footer:#232323;
  --hero:#f0f0f0;
  --text:#555;
  --muted:#888;
  --rose:#e8385a;
  --aqua:#5fcfd3;
  --olive:#8a8019;
  --cyan:#1dc3df;
}
*{box-sizing:border-box;margin:0;padding:0}
html,body{width:1200px;height:1151px;overflow:hidden;background:var(--page);font-family:"Open Sans",sans-serif;color:var(--text)}
.stage{position:absolute;left:0;top:0;width:1320px;height:1266px;transform:scale(.90909);transform-origin:0 0}
.abs{position:absolute}
.topline{left:180px;top:36px;width:960px;height:5px;background:var(--blue)}
.header{left:180px;top:41px;width:960px;height:158px;background:#fff}
.brand{left:204px;top:86px;display:flex;align-items:center;gap:12px;color:var(--blue);font-size:30px;font-weight:600;line-height:1}
.brand-mark{width:66px;height:66px;border-radius:50%;background:var(--blue)}
.brand small{display:block;font-size:21px;font-weight:600;margin-top:6px}
.social{left:985px;top:76px;display:flex;gap:8px}
.social span{width:16px;height:16px;background:#b5b5b5;border-radius:3px}
.phone{left:868px;top:108px;font-size:11px;color:#666}
.search{left:901px;top:126px;width:200px;height:33px;border:1px solid #ddd;font-size:11px;color:#777;padding:10px 9px}
.search svg{position:absolute;right:10px;top:10px}
.nav{left:180px;top:199px;width:960px;height:46px;background:var(--dark);display:flex;padding-left:65px}
.nav a{color:#fff;text-decoration:none;font-size:14px;line-height:46px;padding:0 26px 0 31px;border-right:1px solid #1e1e1e}
.navline{left:180px;top:245px;width:960px;height:6px;background:var(--blue)}
.home{left:190px;top:194px;width:55px;height:55px;background:var(--blue);display:flex;align-items:center;justify-content:center}
.hero{left:181px;top:251px;width:958px;height:451px;background:var(--hero)}
.portrait{left:223px;top:294px;width:270px;height:270px;border-radius:50%;background:#fff;padding:7px}
.portrait div{width:100%;height:100%;border-radius:50%;background:radial-gradient(circle at 45% 40%,#c89a80,#8b6a58 45%,#e5e5e5 70%)}
.hello{left:611px;top:286px;font-size:40px;font-weight:700;color:#555;line-height:1.1}
.about{left:611px;top:338px;font-size:24px;color:#555}
.bubble{top:389px;width:139px;height:139px;border-radius:50%;color:#fff;font-weight:700;font-size:15px;text-align:center;padding-top:46px}
.bubble svg{display:block;margin:0 auto 4px}
.hero-text{left:611px;top:557px;width:495px;font-size:13px;line-height:21px}
.link{color:var(--blue);font-weight:700;font-size:13px;text-decoration:underline}
.content{left:180px;top:702px;width:960px;height:440px;background:#fff}
.dots{left:190px;width:940px;border-top:1px dotted #bbb}
.news-icon{left:216px;top:770px;width:54px;height:54px;border-radius:50%;background:#333}
.news-title{left:299px;top:770px;font-size:24px;color:#555}
.news-text{left:299px;top:816px;width:820px;font-size:13px;line-height:21px}
.card{top:958px;width:295px;height:140px;border:1px solid #ddd}
.card-caption{position:absolute;left:-5px;top:68px;background:rgba(20,20,20,.9);color:#fff;font-size:16px;padding:3px 12px 0;height:53px}
.card-caption b{display:inline-block;margin-top:4px;background:var(--blue);font-size:13px;padding:2px 17px 3px;font-weight:700}
.ticker{left:182px;top:1145px;width:957px;height:58px;background:var(--cyan);color:#fff;font-size:14px;line-height:58px;padding-left:61px}
.ticker-line{left:182px;top:1141px;width:957px;height:4px;background:#ddd}
.ticker i{position:absolute;left:30px;top:21px;width:16px;height:16px;border-radius:50%;background:#fff}
.arrows{position:absolute;right:30px;top:0;font-weight:700;font-size:16px}
.footer{left:182px;top:1203px;width:957px;height:63px;background:var(--footer);color:#aaa;font-size:12px;padding:20px 30px;display:flex;justify-content:space-between}
</style>
</head>
<body>
<div class="stage">
  <div class="abs topline"></div>
  <div class="abs header"></div>
  <div class="abs brand"><span class="brand-mark"></span><div>Dr. Rafael M. Andrade<small>Cirurgia do Quadril</small></div></div>
  <div class="abs social" aria-label="Redes sociais"><span></span><span></span><span></span><span></span><span></span></div>
  <div class="abs phone">Contact Phone:&nbsp; 41 3055-1200 ou 41 3055-1201</div>
  <div class="abs search">Search<svg width="12" height="12" viewBox="0 0 12 12"><circle cx="5" cy="5" r="3.8" fill="none" stroke="#aaa" stroke-width="1.5"/><path d="M8 8l3 3" stroke="#aaa" stroke-width="1.8"/></svg></div>

  <nav class="abs nav"><a>Saiba Mais</a><a>Curriculum lattes</a><a>links</a><a>downloads</a><a>atualidades</a><a>contato</a></nav>
  <div class="abs navline"></div>
  <div class="abs home"><svg width="28" height="26" viewBox="0 0 28 26"><path d="M14 2L1 13h4v12h7v-7h4v7h7V13h4z" fill="#fff"/></svg></div>

  <section class="abs hero"></section>
  <div class="abs portrait"><div role="img" aria-label="Retrato do médico"></div></div>
  <h1 class="abs hello">Hello,</h1>
  <div class="abs about">a bit about me:</div>
  <div class="abs bubble" style="left:611px;background:var(--rose)"><svg width="18" height="22" viewBox="0 0 18 22"><path d="M1 1h11l5 5v15H1z" fill="none" stroke="#fff" stroke-width="2"/><path d="M5 9h8M5 13h8M5 17h8" stroke="#fff" stroke-width="2"/></svg>resume</div>
  <div class="abs bubble" style="left:780px;background:var(--aqua)"><svg width="28" height="22" viewBox="0 0 28 22"><path d="M1 2h11l2 2 2-2h11v18H1z" fill="#fff"/><path d="M14 4v16M4 7h7M4 11h7M4 15h7M17 7h7M17 11h7M17 15h7" stroke="var(--aqua)" stroke-width="1.5"/></svg>manual</div>
  <div class="abs bubble" style="left:949px;background:var(--olive)"><svg width="26" height="22" viewBox="0 0 26 22"><circle cx="7" cy="5" r="4" fill="#fff"/><circle cx="15" cy="5" r="4" fill="#fff"/><rect x="3" y="9" width="16" height="8" fill="#fff"/><path d="M19 11l5-3v10l-5-3z" fill="#fff"/></svg>video</div>
  <p class="abs hero-text">Quisque tristique mauris in aliquet vestibulum. Nulla facilisi. Suspendisse odio lorem, euismod non velit et, congue sagittis sapien. Aenean convallis magna sed est ornare, sit amet eleifend enim feugiat. Morbi tempor consectetur ligula, in sollicitudin nisl pulvinar at.<br><span class="link" style="display:inline-block;margin-top:10px">Continue lendo...</span></p>

  <section class="abs content"></section>
  <div class="abs dots" style="top:744px"></div>
  <div class="abs news-icon"><svg width="54" height="54" viewBox="0 0 54 54"><path d="M27 0A27 27 0 0 1 27 54z" fill="#444"/><path d="M31 18l-9 11h5l-4 8 9-11h-5z" fill="#fff"/></svg></div>
  <h2 class="abs news-title" style="font-weight:400">Atualidades</h2>
  <p class="abs news-text">Quisque tristique mauris in aliquet vestibulum. Nulla facilisi. Suspendisse odio lorem, euismod non velit et, congue sagittis sapien. Aenean convallis magna sed est ornare, sit amet eleifend enim feugiat. Morbi tempor consectetur ligula, in sollicitudin nisl pulvinar at.<br><span class="link" style="display:inline-block;margin-top:10px">Continue...</span></p>
  <div class="abs dots" style="top:912px"></div>

  <div class="abs card" style="left:195px;background:linear-gradient(120deg,#dfe6ea,#a9c4dc 60%,#7fa6cc)" role="img" aria-label="Cirurgião em procedimento de artroscopia"><div class="card-caption">Artroscopia do Quadril<br><b>read more</b></div></div>
  <div class="abs card" style="left:514px;background:linear-gradient(100deg,#1e2530,#2c3a55 45%,#1a1a1a)" role="img" aria-label="Radiografia de prótese do quadril"><div class="card-caption">Prótese do Quadril<br><b>read more</b></div></div>
  <div class="abs card" style="left:835px;background:linear-gradient(135deg,#ece9e4,#dedad3)" role="img" aria-label="Mapa com a localização do consultório"><div class="card-caption">Agende Sua consulta<br><b>view more</b></div></div>

  <div class="abs ticker-line"></div>
  <div class="abs ticker"><i></i>@Você também pode assistir a vídeos ilustrativos em nosso canal do ClipVista<span class="arrows">‹ &nbsp;›</span></div>
  <footer class="abs footer"><span>copyright @ Dr. Rafael Mendes Andrade</span><span>Home | Saiba Mais | Curriculum lattes | Links | Downloads | Atualidades | Contato</span></footer>
</div>
</body>
</html>
```